integrative health clinic-Medical massage, acupuncture, chiropractic

we like our logo, but are open to new ideas. We need a new card design. We have added chiropractic and acupuncture that we have put under the name of the business. We are an integrative medical clinic

Target Market(s)

General public, athletes

Contact Information for Business Card

Phone 5055583927
Fax 5055583926
Hours Monday-Friday 9-6
Saturday 10-6
The 20% can be smaller on the back

Colors
3176b5
0355a3

Requirements
Must have
• Logo but am open to ideas
Nice to have
• We are an integrated medical clinic but also want to be personable. We want the card fun and inviting

```html
<!DOCTYPE html>
<html lang="en">
<head>
<meta charset="utf-8">
<title>Full Motion Wellness – Business Card</title>
<link rel="stylesheet" href="https://fonts.googleapis.com/css2?family=Oswald:wght@400&family=Cormorant+Garamond:ital,wght@1,500&family=Roboto:ital,wght@0,400;1,400;1,500;1,700;1,900&display=swap">
<style>
  :root {
    --backdrop: #d9d4cc;
    --card: #f6f6f6;
    --brand-blue: #2c3d97;
    --ink: #111111;
    --white: #ffffff;
  }
  * { margin: 0; padding: 0; box-sizing: border-box; }
  html, body { width: 900px; height: 1200px; overflow: hidden; }
  body {
    background: var(--backdrop);
    position: relative;
    font-family: "Roboto", Arial, sans-serif;
    color: var(--ink);
  }
  .card {
    position: absolute;
    left: 75px;
    width: 768px;
    background: var(--card);
    border-radius: 18px;
    overflow: hidden;
    box-shadow: 0 6px 14px rgba(0,0,0,0.35);
  }
  .card--front { top: 133px; height: 438px; }
  .card--back { top: 627px; height: 441px; }

  .brand-name {
    position: absolute; left: 147px; top: 50px;
    font-family: "Oswald", "Arial Narrow", sans-serif;
    font-weight: 400; font-size: 50px; line-height: 1; letter-spacing: -0.3px;
    white-space: nowrap;
  }
  .brand-dot {
    position: absolute; left: 180px; top: 118px;
    width: 60px; height: 60px; border-radius: 50%;
    background: var(--brand-blue);
  }
  .brand-tagline {
    position: absolute; left: 258px; top: 115px;
    font-family: "Cormorant Garamond", Georgia, serif;
    font-style: italic; font-weight: 500; font-size: 27px; white-space: nowrap;
  }
  .services {
    position: absolute; left: 0; right: 0; top: 205px;
    text-align: center; font-style: italic; font-size: 19.5px; line-height: 24.5px;
    letter-spacing: 0.7px;
  }
  .contact-band { position: absolute; left: 0; top: 0; }
  .social-badge {
    position: absolute; left: 357px; top: 306px;
    width: 40px; height: 40px; border-radius: 50%;
    background: var(--brand-blue); border: 2.5px solid var(--white);
  }
  .contact {
    position: absolute; left: 0; right: 0; top: 354px;
    text-align: center; color: var(--white); font-size: 19.5px; line-height: 28px;
    letter-spacing: 0.8px; white-space: nowrap;
  }

  .booking-title {
    position: absolute; left: 0; right: 0; top: 82px;
    text-align: center; font-style: italic; font-weight: 900; font-size: 37px;
  }
  .booking-url {
    position: absolute; left: 0; right: 0; top: 126px;
    text-align: center; font-style: italic; font-weight: 700; font-size: 22px;
    letter-spacing: 0.6px;
  }
  .offer-ribbon { position: absolute; left: 0; top: 0; }
  .offer-text {
    position: absolute; left: 202px; width: 362px; top: 203px;
    text-align: center; color: var(--white);
    font-style: italic; font-weight: 700; font-size: 38px; white-space: nowrap;
  }
  .coverage {
    position: absolute; left: 0; right: 0; top: 297px;
    text-align: center; font-style: italic; font-weight: 500; font-size: 22px; line-height: 28px;
    letter-spacing: 0.5px;
  }
</style>
</head>
<body>
  <section class="card card--front">
    <h1 class="brand-name">Full Motion Wellness</h1>
    <span class="brand-dot"></span>
    <p class="brand-tagline">Sports Therapy and Wellness Center</p>
    <p class="services">Specialzing in<br>Medcal, Chiropractic &amp; Acupuncture,<br>Sports Massage &amp; Manual Therapies</p>
    <svg class="contact-band" width="768" height="438" viewBox="0 0 768 438">
      <path d="M0 272 Q384 345 768 276 L768 438 L0 438 Z" fill="var(--brand-blue)"/>
    </svg>
    <span class="social-badge"></span>
    <p class="contact">P: (505) 558 - 3927 &nbsp;&nbsp;| E: Info@fullmotionwellnessnm.com<br>742 Alder Ln, Ste 4, Riverton, Co 80911</p>
  </section>

  <section class="card card--back">
    <h2 class="booking-title">BOOK ONLINE</h2>
    <p class="booking-url">www.fullmotionwellnessnm.com</p>
    <svg class="offer-ribbon" width="768" height="441" viewBox="0 0 768 441">
      <path d="M125 215 L191 215 L191 266 L125 266 L148 240 Z" fill="var(--brand-blue)"/>
      <path d="M575 215 L641 215 L618 240 L641 266 L575 266 Z" fill="var(--brand-blue)"/>
      <rect x="202" y="200" width="362" height="58" fill="var(--brand-blue)"/>
    </svg>
    <p class="offer-text">20% Off First Visit</p>
    <p class="coverage">We Accept some insurances,<br>Worker’s Comp &amp; Personal Injury</p>
  </section>
</body>
</html>
```